VLM8 Business Card Design Project

Design which catches the client with the first impression. A design which is professional and classy with elegance. We have also got another project running and the winning prize for that is $240 "vlm8 print + graphic design".
For all the company details please visit www.vlm8-example.com.
Please find the logo attached and i would like to have good colors for my business card.
, Design which catches the client with the first impression. A design which is professional and classy with elegance.
Updates
VLM8 is running two projects at the same time, please feel free to participate. The other project name is

```html
<!DOCTYPE html>
<html lang="en">
<head>
<meta charset="utf-8">
<title>VLM8 Business Card Design</title>
<link href="https://fonts.googleapis.com/css2?family=Michroma&family=Signika:wght@400&display=swap" rel="stylesheet">
<style>
  :root {
    --page-bg: #d9d9d9;
    --grey-light: #8f8f8f;
    --grey-dark: #4f4f4f;
    --grey2-light: #9c9c9c;
    --grey2-dark: #474747;
    --teal-light: #86d8bf;
    --teal-dark: #3d977f;
    --cyan: #3ec6da;
    --yellow: #e4e43a;
    --name-pale: rgba(255,255,255,0.38);
    --name-dark: rgba(40,40,40,0.75);
    --name-teal: rgba(210,245,236,0.6);
    --stripe: rgba(255,255,255,0.09);
  }
  * { margin: 0; padding: 0; box-sizing: border-box; }
  html, body { width: 1200px; height: 2434px; overflow: hidden; background: var(--page-bg); }
  .canvas { position: relative; width: 1200px; height: 2434px; }
  .card {
    position: absolute; left: 122px; width: 956px; height: 546px; overflow: hidden;
    box-shadow: 3px 4px 6px rgba(0,0,0,0.35);
  }
  .card::before {
    content: ""; position: absolute; inset: 0;
    background: repeating-linear-gradient(180deg, var(--stripe) 0 3px, transparent 3px 8px);
  }
  .card--caps { top: 114px; background: linear-gradient(90deg, var(--grey-light), var(--grey-dark)); }
  .card--grey { top: 905px; background: linear-gradient(90deg, var(--grey2-light), var(--grey2-dark)); }
  .card--teal { top: 1767px; background: linear-gradient(90deg, var(--teal-light), var(--teal-dark)); }
  .contact {
    position: absolute; right: 20px; top: 22px; text-align: right; list-style: none;
  }
  .card--caps .contact { font-family: "Michroma", sans-serif; font-size: 25px; line-height: 33px; text-transform: uppercase; color: var(--cyan); }
  .card--grey .contact, .card--teal .contact { font-family: "Signika", sans-serif; font-size: 31px; line-height: 46px; }
  .card--grey .contact { color: var(--cyan); }
  .card--teal .contact { color: var(--yellow); }
  .contact .web { color: var(--yellow); }
  .brand-name { position: absolute; inset: 0; width: 956px; height: 546px; }
  .brand-name text { font-size: 215px; }
  .card--caps .brand-name text { font-family: "Michroma", sans-serif; font-size: 175px; fill: var(--name-pale); }
  .card--grey .brand-name text { font-family: "Signika", sans-serif; fill: var(--name-dark); }
  .card--teal .brand-name text { font-family: "Signika", sans-serif; fill: var(--name-teal); }
  .brand-dot {
    position: absolute; left: 110px; top: 240px; width: 100px; height: 100px; border-radius: 50%;
  }
  .card--caps .brand-dot { background: var(--name-pale); }
  .card--grey .brand-dot { background: var(--name-dark); }
  .card--teal .brand-dot { background: var(--name-teal); }
</style>
</head>
<body>
<main class="canvas">
  <section class="card card--caps">
    <ul class="contact">
      <li>318 Harbor Lane 07</li>
      <li>9&nbsp; Street Dalworth</li>
      <li>Linfield Crestor 318640</li>
      <li>Call 555_010_2468</li>
      <li class="web">www.vlm8-example.com</li>
    </ul>
    <span class="brand-dot"></span>
    <svg class="brand-name" viewBox="0 0 956 546" aria-label="VLM8">
      <text x="272" y="538" textLength="677" lengthAdjust="spacingAndGlyphs">VLM8</text>
    </svg>
  </section>

  <section class="card card--grey">
    <ul class="contact">
      <li>318 harbor lane 07</li>
      <li>9&nbsp; street dalworth</li>
      <li>linfield crestor 318640</li>
      <li>call 555_010_2468</li>
      <li class="web">www.vlm8-example.com</li>
    </ul>
    <span class="brand-dot"></span>
    <svg class="brand-name" viewBox="0 0 956 546" aria-label="VLM8">
      <text x="272" y="538" textLength="677" lengthAdjust="spacing">VLM8</text>
    </svg>
  </section>

  <section class="card card--teal">
    <ul class="contact">
      <li>318 harbor lane 07</li>
      <li>9&nbsp; street dalworth</li>
      <li>linfield crestor 318640</li>
      <li>call 555_010_2468</li>
      <li class="web">www.vlm8-example.com</li>
    </ul>
    <span class="brand-dot"></span>
    <svg class="brand-name" viewBox="0 0 956 546" aria-label="VLM8">
      <text x="272" y="538" textLength="677" lengthAdjust="spacing">VLM8</text>
    </svg>
  </section>
</main>
</body>
</html>
```